Kveldbrá - Start-up company selling electricity

Hello let me tell you about Kveldbrá.

Kveldbrá is start-up company selling electricity in Iceland. The operations of the company consist of making power usage forecasts for our customers, purchasing the electricity wholesale from the energy producers, and selling the electricity to the consumer. We are focused on tech by using optimization and machine learning to minimize electricity prices to our customers. Our marketing strategy is to portray a tech company mindset and to show dedication to driving down the electricity price on the market.

We need your help to make our website pop. Possible concepts to work with are as follows:

- Iceland the land of ice and fire
- Green energy
- Innovation
- Tech and data science

Link to our website: https://prufa.kveldbra.is/
We are open to ideas.
Thank you!

Target Market(s)

Electricity consumers both homes and companies.

Number of Pages Required

1 page

Font styles to use
Serif
Sans Serif

```html
<!DOCTYPE html>
<html lang="en">
<head>
<meta charset="utf-8">
<title>Kveldbrá – Same Electricity Just Cheaper</title>
<link rel="stylesheet" href="https://fonts.googleapis.com/css2?family=Poppins:wght@400;500;600;700&display=swap">
<style>
:root{
  --green:#8cc63f;
  --green-bright:#84c225;
  --black:#000;
  --charcoal:#262626;
  --panel:#f1f1f1;
  --white:#fff;
  --text:#222;
}
*{box-sizing:border-box;margin:0;padding:0}
html,body{width:1200px;height:3750px;overflow:hidden;background:#fff;font-family:"Poppins",Arial,sans-serif;color:var(--text)}
.board{position:relative;height:762px;background:#fff}
.board-name{position:absolute;top:190px;left:0;width:1200px;display:flex;justify-content:center;align-items:center;gap:26px;font-size:84px;font-weight:700;letter-spacing:2px;color:var(--black)}
.board-name .dot{width:64px;height:64px;border-radius:50%;background:var(--green-bright)}
.type-sample{position:absolute;top:420px;left:276px;font-size:50px;font-weight:600;color:var(--charcoal);letter-spacing:2px}
.swatch{position:absolute;top:410px;width:90px;height:78px;border-radius:10px}
.swatch.green{left:614px;background:var(--green-bright)}
.swatch.black{left:721px;background:var(--black)}
.swatch.charcoal{left:827px;background:var(--charcoal)}

.site{position:relative;width:1200px}
section,.footer{position:relative;overflow:hidden;width:1200px;display:block}
.brand{font-weight:600;color:#fff;font-size:27px;letter-spacing:1px;display:flex;align-items:center;gap:10px;white-space:nowrap}
.brand .dot{width:22px;height:22px;border-radius:50%;background:#fff}

.hero{height:573px;background:radial-gradient(ellipse at 40% 70%,#2a2a2a 0%,#111 45%,#000 80%)}
.hero svg{position:absolute;left:0;top:0}
.hero .brand{position:absolute;left:94px;top:40px}
.nav{position:absolute;top:52px;left:628px;display:flex;gap:29px;font-size:12.5px;font-weight:500;color:#fff;white-space:nowrap}
.hero h1{position:absolute;left:94px;top:204px;font-size:44px;line-height:48px;font-weight:600;color:#fff}
.hero h1 span{color:var(--green)}
.hero p{position:absolute;left:94px;top:318px;width:420px;font-size:11.5px;line-height:18.5px;color:#fff}
.btn-outline{position:absolute;left:94px;top:409px;width:140px;height:34px;border:1.5px solid #fff;border-radius:17px;color:#fff;font-size:11px;font-weight:500;display:flex;align-items:center;justify-content:center}

.about{height:472px;background:#fff}
.about .visual{position:absolute;left:183px;top:78px;width:205px;height:312px;border-radius:90px 90px 102px 102px;background:linear-gradient(180deg,#2fd1a4 0%,#1a8f86 45%,#2b5f86 70%,#c77a4a 100%)}
.about h2{position:absolute;left:518px;top:85px;font-size:38px;font-weight:600;color:#000}
.about h2 span{color:var(--green)}
.about .copy{position:absolute;left:518px;top:150px;width:545px;font-size:12.3px;line-height:17.5px;color:#222}
.about .copy p+p{margin-top:17px}

.sell{height:564px;background:radial-gradient(ellipse at 50% 40%,#1c1c1c 0%,#050505 70%)}
.sell h2{position:absolute;top:60px;width:1200px;text-align:center;font-size:29px;font-weight:600;color:#fff}
.sell h2 span{color:var(--green)}
.card{position:absolute;top:160px;width:295px;height:308px;background:#fff}
.card.business{left:96px}
.card.price{left:454px;background:var(--green)}
.card.future{left:810px}
.card svg{position:absolute}
.card .label{position:absolute;font-size:14px;color:#222;white-space:nowrap}
.card.business .label{left:83px;top:48px}
.card.future .label{left:70px;top:52px}
.btn-block{position:absolute;left:32px;width:239px;height:50px;display:flex;align-items:center;justify-content:center;font-size:14px;font-weight:500}
.btn-block.dark{top:135px;background:#000;color:#fff}
.btn-block.light{top:211px;background:var(--green);color:#fff}
.card.price .label{left:0;top:52px;width:100%;text-align:center;color:#fff}
.price-figure{position:absolute;left:0;width:100%;text-align:center;color:#fff}
.price-figure b{display:block;font-size:28px;font-weight:500;line-height:30px}
.price-figure small{display:block;font-size:9.5px;letter-spacing:.5px}
.price-figure.one{top:92px}
.price-figure.two{top:150px}
.price-links{position:absolute;top:236px;width:100%;text-align:center;color:#fff;font-size:13px;line-height:26px}
.card.future p{position:absolute;left:30px;top:117px;width:235px;text-align:center;font-size:12.7px;line-height:22px;color:#222}

.feature{background:#fff}
.feature .photo{position:absolute}
.feature .text{position:absolute;background:var(--panel)}
.feature h3{font-size:34px;font-weight:600;color:var(--green);letter-spacing:.5px;white-space:nowrap}
.feature h3 span{color:#000}
.feature p{font-size:9.6px;line-height:24.5px;color:#222;width:440px;margin-top:14px}
.btn-read{display:flex;align-items:center;justify-content:center;width:160px;height:42px;background:var(--green);color:#fff;font-size:14px;font-weight:600;margin-top:14px}
.innovation{height:354px}
.innovation .photo{left:0;top:32px;width:543px;height:322px;background:linear-gradient(180deg,#2a5a9a 0%,#8aa6c9 35%,#f6c56a 52%,#556f86 62%,#3f5f3a 100%)}
.innovation .text{left:543px;top:32px;width:657px;height:322px;padding:44px 0 0 112px}
.land{height:443px}
.land .text{left:0;top:0;width:655px;height:443px;background:#fff;padding:92px 0 0 103px}
.land .photo{left:655px;top:52px;width:545px;height:323px;background:linear-gradient(160deg,#6e7274 0%,#b9bcbd 35%,#3b2b24 55%,#d24a12 63%,#e8e9ea 80%,#f3f3f3 100%)}
.tech{height:356px}
.tech .photo{left:0;top:0;width:547px;height:324px;background:linear-gradient(135deg,#0a1c4a 0%,#0d5ec7 40%,#15a2e6 60%,#0b2a74 100%)}
.tech .text{left:547px;top:0;width:653px;height:324px;padding:42px 0 0 103px}

.footer{height:226px;background:#000;color:#fff}
.footer .brand{position:absolute;left:98px;top:40px;font-size:30px}
.footer .about-line{position:absolute;left:104px;top:92px;width:240px;font-size:7.8px;line-height:11px}
.fcol{position:absolute;top:60px;font-size:8.6px;line-height:14px;white-space:nowrap}
.fcol h4{font-size:8.6px;font-weight:500;margin-bottom:12px}
.fcol.links{left:412px}
.fcol.address{left:594px}
.fcol.contact{left:782px}
.fcol.follow{left:1026px}
.copyright{position:absolute;bottom:6px;left:0;width:1200px;text-align:center;font-size:9px;letter-spacing:.8px}
</style>
</head>
<body>

<div class="board">
  <div class="board-name"><span class="dot"></span>KVELDBRÁ</div>
  <div class="type-sample">AAA&nbsp; aaa</div>
  <div class="swatch green"></div>
  <div class="swatch black"></div>
  <div class="swatch charcoal"></div>
</div>

<main class="site">
  <section class="hero">
    <svg width="1200" height="573" viewBox="0 0 1200 573">
      <defs>
        <linearGradient id="rooftops" x1="0" y1="0" x2="1" y2="1">
          <stop offset="0" stop-color="#6f8d56"/>
          <stop offset=".5" stop-color="#3f5a3a"/>
          <stop offset="1" stop-color="#8a5a48"/>
        </linearGradient>
      </defs>
      <circle cx="958" cy="340" r="290" fill="none" stroke="var(--green)" stroke-width="7"/>
      <circle cx="975" cy="352" r="283" fill="url(#rooftops)" role="img" aria-label="Aerial photo of a residential neighbourhood with coloured rooftops"/>
    </svg>
    <div class="brand"><span class="dot"></span>KVELDBRÁ</div>
    <nav class="nav"><span>TERMS OF BUSINESS</span><span>QUESTION &amp; ANSWER</span><span>ABOUT</span><span>KVELDBRÁ</span></nav>
    <h1>Same Electricity<br><span>Just Cheaper!</span></h1>
    <p>Lorem Ipsum is simply dummy text of the printing and typesetting industry. Lorem Ipsum has been the industry's standard dummy text ever since the 1500s, when an unknown printer took a galley of type and scrambled it to make a type specimen book.</p>
    <div class="btn-outline">GET STARTED</div>
  </section>

  <section class="about">
    <div class="visual" role="img" aria-label="Illustration of aurora over a snowy Icelandic village"></div>
    <h2>About <span>Kveldbrá</span></h2>
    <div class="copy">
      <p>Kveldbrá uses automation and artificial intelligence to achieve lower prices in the electricity market. Our goal is to minimize the cost of energy sales, promote energy balance and offer good service.</p>
      <p>Kveldbrá's goal is to offer its customers the most favorable electricity prices in Iceland. Electricity is part of the monthly costs of households and companies, and by doing business with Kveldbrá, savings can be achieved and operating costs reduced. Kveldbrá wants to make the electricity system "smarter". Data science and the use of artificial intelligence can maximize the efficiency of the electricity system, minimize electricity costs and promote energy balance. Therefore, it can be said that by trading with Kveldbrá, you support the development of the Icelandic electricity market.</p>
    </div>
  </section>

  <section class="sell">
    <h2>We sell <span>electricity</span> ~ join and <span>pay less!</span></h2>
    <div class="card business">
      <svg style="left:34px;top:36px" width="34" height="56" viewBox="0 0 34 56" fill="none" stroke="var(--green)" stroke-width="2">
        <path d="M10 2v10M24 2v10M4 12h26v14a13 13 0 0 1-26 0z"/><path d="M18 18l-4 8h6l-4 8"/><path d="M17 39v15"/>
      </svg>
      <span class="label">Welcome To Business</span>
      <div class="btn-block dark">Company</div>
      <div class="btn-block light">Home</div>
    </div>
    <div class="card price">
      <svg style="left:28px;top:40px" width="60" height="42" viewBox="0 0 60 42" fill="none" stroke="#fff" stroke-width="2">
        <path d="M10 14c6-8 30-10 40 0 4 4 6 8 6 12h-4c-2 6-6 8-6 8v6h-6v-4H22v4h-6v-6c-4-2-8-6-8-10H4v-6h4z"/><circle cx="30" cy="20" r="7"/><path d="M30 15v10"/>
      </svg>
      <span class="label">Price</span>
      <div class="price-figure one"><b>6.95</b><small>ISK / KWh</small></div>
      <div class="price-figure two"><b>6.22</b><small>ISK / KWh</small></div>
      <div class="price-links">electric acceleration<br>make a price comparison</div>
    </div>
    <div class="card future">
      <svg style="left:22px;top:40px" width="34" height="42" viewBox="0 0 34 42" fill="none" stroke="var(--green)" stroke-width="2">
        <path d="M20 2L4 24h12l-4 16 18-24H18z"/>
      </svg>
      <span class="label">the future is exciting</span>
      <p>Let's make the electricity system smarter together. Kveldbrá uses artificial intelligence, data science, and automation to minimize costs and promote eccentricity</p>
    </div>
  </section>

  <section class="feature innovation">
    <div class="photo" role="img" aria-label="Photo of solar panels at sunset with a city skyline"></div>
    <div class="text">
      <h3>INNOVATION</h3>
      <p>Lorem Ipsum is simply dummy text of the printing and typesetting industry. Lorem Ipsum has been the industry's standard dummy text ever since the 1500s, when an unknown printer took a galley of type and scrambled it to make a type specimen book. It has survived not only five centuries, but also the leap into electronic typesetting, remaining essentially unchanged.</p>
      <div class="btn-read">READ MORE</div>
    </div>
  </section>

  <section class="feature land">
    <div class="text">
      <h3><span>THE LAND OF</span> ICE AND FIRE</h3>
      <p>Lorem Ipsum is simply dummy text of the printing and typesetting industry. Lorem Ipsum has been the industry's standard dummy text ever since the 1500s, when an unknown printer took a galley of type and scrambled it to make a type specimen book. It has survived not only five centuries, but also the leap into electronic typesetting, remaining essentially unchanged.</p>
      <div class="btn-read">READ MORE</div>
    </div>
    <div class="photo" role="img" aria-label="Photo of glowing lava flowing across snow under steam"></div>
  </section>

  <section class="feature tech">
    <div class="photo" role="img" aria-label="Photo of blue glowing data grid technology"></div>
    <div class="text">
      <h3>TECH <span>AND</span> DATA SCIENCE</h3>
      <p>Lorem Ipsum is simply dummy text of the printing and typesetting industry. Lorem Ipsum has been the industry's standard dummy text ever since the 1500s, when an unknown printer took a galley of type and scrambled it to make a type specimen book. It has survived not only five centuries, but also the leap into electronic typesetting, remaining essentially unchanged.</p>
      <div class="btn-read">READ MORE</div>
    </div>
  </section>

  <footer class="footer">
    <div class="brand"><span class="dot"></span>KVELDBRÁ</div>
    <p class="about-line">the operations of the company consist of making power usage forecasts for our customers, purchasing the electricity wholesale from the energy producers and selling the electricity to the consumer.</p>
    <div class="fcol links"><h4>QUICK LINKS</h4>terms of business<br>question and answer<br>about kveldbrá</div>
    <div class="fcol address"><h4>ADDRESS</h4>LJÓSAVEGUR 4, 170<br>DÆMABÆR</div>
    <div class="fcol contact"><h4>CONTACT US</h4>hallo@kveldbra.is<br>555-0142</div>
    <div class="fcol follow"><h4>FOLLOW US</h4></div>
    <div class="copyright">copyright © kveldbrá 2021 all rights reserved</div>
  </footer>
</main>

</body>
</html>
```